Old Fashioned, Artisan Goat Milk Soap Label

We are branching out in our goat milk dairy into artisan goat milk soaps. High quality, yet an old fashioned feel. Simple yet elegant. Emphasis on the milk and its moisturizing, healing, softening, and superiority.
Purity in a simple design that harkens back to a quaint, earlier time where quality ingredients were valued as much as quality workmanship.
Perhaps a drop symbolizing the milk, or a bucket pouring into or out of the logo. We already have our farm logo, Whistling Brook, and were thinking the soap would be "Dotty Mae"
The labels will grace our liquid soap bottles and our bar soaps. 3.5" X 2.5"
The label color will be an antiqued ivory or other shade to convey a simpler time.

Reason: Realized that the contest length was short enough to scare away designers. Adding time to give entered designers time to create.

Target Market(s)

Upscale people looking to know where their products come from. People looking for better options, artisan products.

Requirements
Must have
• My project must have emphasis on the milk, old time feel, simple elegance
Nice to have
• Perhaps a drop symbolizing the milk, or a bucket pouring into or out of the logo. We already have our farm logo, Whistling Brook, and were thinking the soap would be "Dotty Mae"
• If you use a goat, please be aware that we have the breed Nubians that have long luxurious ears and don't have horns.

```html
<!DOCTYPE html>
<html lang="en">
<head>
<meta charset="utf-8">
<title>Dotty Mae Goat Milk Soap – Label Colourways</title>
<link href="https://fonts.googleapis.com/css2?family=Oswald:wght@300&family=Playfair+Display+SC:wght@700&display=swap" rel="stylesheet">
<style>
  :root{
    --slate:#7b93a1;
    --sage:#a8c3bc;
    --ivory:#fcf8d4;
    --peach:#f5d9be;
    --teal:#82b1a2;
    --gutter:#ffffff;
  }
  html,body{margin:0;padding:0;overflow:hidden;background:var(--gutter);}
  .sheet{
    width:1200px;height:810px;
    display:grid;grid-template-columns:598px 598px;grid-template-rows:404px 404px;
    gap:2px 4px;
  }
  .label{
    position:relative;overflow:hidden;
    background:var(--band);
    color:var(--ink);
  }
  .label__field{
    position:absolute;left:0;right:0;top:65px;height:272px;
    background:var(--field);
  }
  .label__frame{position:absolute;left:0;top:0;width:598px;height:404px;}
  .label__frame .line{fill:none;stroke:var(--ink);stroke-width:1.6;}
  .label__frame .dot{fill:var(--ink);}
  .label__frame .ornament{fill:var(--ink);opacity:.35;}
  .label__text{position:absolute;left:0;width:598px;text-align:center;margin:0;line-height:1;}
  .label__kicker{
    top:148px;font-family:"Oswald",sans-serif;font-weight:300;
    font-size:21px;letter-spacing:.42em;padding-left:.42em;
  }
  .label__name{
    top:174px;font-family:"Playfair Display SC",serif;font-weight:700;
    font-size:52px;letter-spacing:.02em;
  }
  .label__product{
    top:238px;font-family:"Oswald",sans-serif;font-weight:300;
    font-size:23px;letter-spacing:.32em;padding-left:.32em;
  }
  .label--slate{--band:var(--sage);--field:var(--slate);--ink:var(--ivory);}
  .label--ivory-slate{--band:var(--slate);--field:var(--ivory);--ink:var(--slate);}
  .label--ivory-teal{--band:var(--peach);--field:var(--ivory);--ink:var(--teal);}
  .label--teal{--band:var(--sage);--field:var(--teal);--ink:var(--ivory);}
</style>
</head>
<body>
<main class="sheet">
  <section class="label label--slate">
    <div class="label__field"></div>
    <svg class="label__frame" viewBox="0 0 598 404" aria-hidden="true">
      <path class="line" d="M101 137 Q300 92 494 137"/>
      <path class="line" d="M101 267 Q300 312 494 267"/>
      <path class="line" d="M211 133 H389"/><path class="dot" d="M300 129 l4 4 -4 4 -4 -4z"/>
      <path class="line" d="M211 270 H389"/><path class="dot" d="M300 266 l4 4 -4 4 -4 -4z"/>
    </svg>
    <svg class="label__frame" viewBox="0 0 598 404">
      <rect class="ornament" role="img" aria-label="Scrolled flourish crest above the frame" x="245" y="76" width="110" height="40" rx="20"/>
      <rect class="ornament" role="img" aria-label="Scrolled flourish crest below the frame" x="245" y="282" width="110" height="44" rx="20"/>
      <rect class="ornament" role="img" aria-label="Corner scroll flourish" x="42" y="140" width="50" height="30" rx="15"/>
      <rect class="ornament" role="img" aria-label="Corner scroll flourish" x="42" y="228" width="50" height="32" rx="15"/>
      <rect class="ornament" role="img" aria-label="Corner scroll flourish" x="506" y="140" width="50" height="30" rx="15"/>
      <rect class="ornament" role="img" aria-label="Corner scroll flourish" x="506" y="228" width="50" height="32" rx="15"/>
    </svg>
    <p class="label__text label__kicker">HANDCRAFTED</p>
    <h1 class="label__text label__name">DOTTY MAE</h1>
    <p class="label__text label__product">GOAT MILK SOAP</p>
  </section>

  <section class="label label--ivory-slate">
    <div class="label__field"></div>
    <svg class="label__frame" viewBox="0 0 598 404" aria-hidden="true">
      <path class="line" d="M101 137 Q300 92 494 137"/>
      <path class="line" d="M101 267 Q300 312 494 267"/>
      <path class="line" d="M211 133 H389"/><path class="dot" d="M300 129 l4 4 -4 4 -4 -4z"/>
      <path class="line" d="M211 270 H389"/><path class="dot" d="M300 266 l4 4 -4 4 -4 -4z"/>
    </svg>
    <svg class="label__frame" viewBox="0 0 598 404">
      <rect class="ornament" role="img" aria-label="Scrolled flourish crest above the frame" x="245" y="76" width="110" height="40" rx="20"/>
      <rect class="ornament" role="img" aria-label="Scrolled flourish crest below the frame" x="245" y="282" width="110" height="44" rx="20"/>
      <rect class="ornament" role="img" aria-label="Corner scroll flourish" x="42" y="140" width="50" height="30" rx="15"/>
      <rect class="ornament" role="img" aria-label="Corner scroll flourish" x="42" y="228" width="50" height="32" rx="15"/>
      <rect class="ornament" role="img" aria-label="Corner scroll flourish" x="506" y="140" width="50" height="30" rx="15"/>
      <rect class="ornament" role="img" aria-label="Corner scroll flourish" x="506" y="228" width="50" height="32" rx="15"/>
    </svg>
    <p class="label__text label__kicker">HANDCRAFTED</p>
    <h2 class="label__text label__name">DOTTY MAE</h2>
    <p class="label__text label__product">GOAT MILK SOAP</p>
  </section>

  <section class="label label--ivory-teal">
    <div class="label__field"></div>
    <svg class="label__frame" viewBox="0 0 598 404" aria-hidden="true">
      <path class="line" d="M101 137 Q300 92 494 137"/>
      <path class="line" d="M101 267 Q300 312 494 267"/>
      <path class="line" d="M211 133 H389"/><path class="dot" d="M300 129 l4 4 -4 4 -4 -4z"/>
      <path class="line" d="M211 270 H389"/><path class="dot" d="M300 266 l4 4 -4 4 -4 -4z"/>
    </svg>
    <svg class="label__frame" viewBox="0 0 598 404">
      <rect class="ornament" role="img" aria-label="Scrolled flourish crest above the frame" x="245" y="76" width="110" height="40" rx="20"/>
      <rect class="ornament" role="img" aria-label="Scrolled flourish crest below the frame" x="245" y="282" width="110" height="44" rx="20"/>
      <rect class="ornament" role="img" aria-label="Corner scroll flourish" x="42" y="140" width="50" height="30" rx="15"/>
      <rect class="ornament" role="img" aria-label="Corner scroll flourish" x="42" y="228" width="50" height="32" rx="15"/>
      <rect class="ornament" role="img" aria-label="Corner scroll flourish" x="506" y="140" width="50" height="30" rx="15"/>
      <rect class="ornament" role="img" aria-label="Corner scroll flourish" x="506" y="228" width="50" height="32" rx="15"/>
    </svg>
    <p class="label__text label__kicker">HANDCRAFTED</p>
    <h2 class="label__text label__name">DOTTY MAE</h2>
    <p class="label__text label__product">GOAT MILK SOAP</p>
  </section>

  <section class="label label--teal">
    <div class="label__field"></div>
    <svg class="label__frame" viewBox="0 0 598 404" aria-hidden="true">
      <path class="line" d="M101 137 Q300 92 494 137"/>
      <path class="line" d="M101 267 Q300 312 494 267"/>
      <path class="line" d="M211 133 H389"/><path class="dot" d="M300 129 l4 4 -4 4 -4 -4z"/>
      <path class="line" d="M211 270 H389"/><path class="dot" d="M300 266 l4 4 -4 4 -4 -4z"/>
    </svg>
    <svg class="label__frame" viewBox="0 0 598 404">
      <rect class="ornament" role="img" aria-label="Scrolled flourish crest above the frame" x="245" y="76" width="110" height="40" rx="20"/>
      <rect class="ornament" role="img" aria-label="Scrolled flourish crest below the frame" x="245" y="282" width="110" height="44" rx="20"/>
      <rect class="ornament" role="img" aria-label="Corner scroll flourish" x="42" y="140" width="50" height="30" rx="15"/>
      <rect class="ornament" role="img" aria-label="Corner scroll flourish" x="42" y="228" width="50" height="32" rx="15"/>
      <rect class="ornament" role="img" aria-label="Corner scroll flourish" x="506" y="140" width="50" height="30" rx="15"/>
      <rect class="ornament" role="img" aria-label="Corner scroll flourish" x="506" y="228" width="50" height="32" rx="15"/>
    </svg>
    <p class="label__text label__kicker">HANDCRAFTED</p>
    <h2 class="label__text label__name">DOTTY MAE</h2>
    <p class="label__text label__product">GOAT MILK SOAP</p>
  </section>
</main>
</body>
</html>
```